A wine Label for a new brand of New Zealand Wine

We are looking for a Wine Label for our "Harbor Crest" brand of wines from North Otago New Zealand. We would like the label to perhaps use the HC as a logo and the rest up to the designer. We have our vineyards located in the Waitaki Valley New Zealand which is a southern region with mountains and a river flowing past our vineyard. Photos attached of Dramatic Landscape. Also attached is a basic outline of requirements for the front bottle of the label. The rear bottle label will contain writing about the wines background plus statutory regulations on Alc. Vol, bar code etc. Front Label size to be no Larger than 80mm deep by 100 mm wide. The label can be simple or graphic, whatever the designer chooses.
Target Market(s)
New Wine Brand
Look and feel
Each slider illustrates characteristics of the customer's brand and the style your logo design should communicate.

```html
<!DOCTYPE html>
<html lang="en">
<head>
<meta charset="utf-8">
<title>Harbor Crest Pinot Gris 2015 – Front Labels</title>
<link href="https://fonts.googleapis.com/css2?family=Cinzel:wght@400;500&family=Cormorant+Garamond:ital,wght@1,600&display=swap" rel="stylesheet">
<style>
  :root {
    --page-bg: #e3e9ec;
    --label-light: #ececee;
    --label-dark: #c6c7ca;
    --gold: #b38a2c;
    --ink: #2a2a2c;
    --taupe-light: #d9d1c8;
    --taupe-mid: #b3a695;
    --taupe-dark: #8f8270;
    --green-light: #bfe0cf;
    --green-mid: #5eae83;
    --green-dark: #17873f;
  }
  * { margin: 0; padding: 0; box-sizing: border-box; }
  html, body { width: 785px; height: 1200px; overflow: hidden; }
  body {
    background: var(--page-bg);
    display: flex;
    align-items: center;
    justify-content: center;
    gap: 25px;
  }
  .label {
    position: relative;
    width: 360px;
    height: 428px;
    background: linear-gradient(135deg, var(--label-light) 0%, #dcdde0 45%, var(--label-dark) 100%);
    text-align: center;
    color: var(--ink);
    font-family: "Cinzel", serif;
    box-shadow: 0 2px 8px rgba(0,0,0,0.12);
  }
  .brand {
    position: absolute;
    top: 0;
    left: 0;
    right: 0;
    display: flex;
    flex-direction: column;
    align-items: center;
  }
  .brand-square {
    width: 72px;
    height: 72px;
    background: var(--gold);
  }
  .brand-name {
    margin-top: 10px;
    font-family: "Cinzel", serif;
    font-weight: 400;
    font-size: 22px;
    line-height: 26px;
    color: var(--gold);
    letter-spacing: 0.5px;
  }
  .varietal {
    position: absolute;
    top: 202px;
    left: 0;
    right: 0;
    font-size: 27px;
    font-weight: 400;
    letter-spacing: 2px;
  }
  .vintage {
    position: absolute;
    top: 245px;
    left: 0;
    right: 0;
    font-size: 16px;
    letter-spacing: 3px;
  }
  .origin {
    position: absolute;
    top: 288px;
    left: 0;
    right: 0;
    font-size: 10.5px;
    letter-spacing: 0.6px;
  }
  .landscape {
    position: absolute;
    left: 0;
    right: 0;
    bottom: 0;
    height: 128px;
  }
  .landscape--taupe {
    background: linear-gradient(180deg, var(--label-light) 0%, var(--taupe-light) 20%, var(--taupe-mid) 55%, var(--taupe-dark) 100%);
  }
  .landscape--green {
    background: linear-gradient(180deg, var(--label-light) 0%, var(--green-light) 20%, var(--green-mid) 50%, var(--green-dark) 100%);
  }
  .region {
    position: absolute;
    left: 0;
    right: 0;
    bottom: 8px;
    font-family: "Cormorant Garamond", serif;
    font-style: italic;
    font-weight: 600;
    font-size: 11.5px;
    color: #ffffff;
    letter-spacing: 0.4px;
  }
</style>
</head>
<body>
  <section class="label label--taupe">
    <div class="brand">
      <div class="brand-square"></div>
      <div class="brand-name">HARBOR<br>CREST</div>
    </div>
    <h1 class="varietal">PINOT GRIS</h1>
    <p class="vintage">2015</p>
    <p class="origin">NEW ZEALAND WINE</p>
    <div class="landscape landscape--taupe" role="img" aria-label="Layered taupe mountain ranges of the valley"></div>
    <p class="region">Waitaki Valley North Otago</p>
  </section>

  <section class="label label--green">
    <div class="brand">
      <div class="brand-square"></div>
      <div class="brand-name">HARBOR<br>CREST</div>
    </div>
    <h1 class="varietal">PINOT GRIS</h1>
    <p class="vintage">2015</p>
    <p class="origin">NEW ZEALAND WINE</p>
    <div class="landscape landscape--green" role="img" aria-label="Layered green mountain ranges of the valley"></div>
    <p class="region">Waitaki Valley North Otago</p>
  </section>
</body>
</html>
```